Plate Parade! Digital Order Web App

This is a web app on mobile phone, for consumers to order food inside a restaurant using their phones. we have done up the flow but we need to revamp UI design. pls have a look at our current web on your mobile phone:
https://demo.pesanly.app/o/KWLM/274615

CURRENT DESIGN.
1. food category on left side, always shown. menu items in list view with image.
2. when we click on an item, there is popup page, to select modifiers, or quantity.
3. order review page(cart page) is quite messy now, need a complete new look.
4 payment page(no need to design, handle by Paxtel)
5. order confirmation page. success or error return

DESIGN requirements:
please browse through and click to order with current page above. we have put in lots of thoughts and effort for current flow, the new design should base on this flow.
1. web app. no zoom in/out is allowed for users. responsive html to suit different mobile phone screen size. modern fonts.
2. PAGES needed:
home/welcome page,
well laid out menu items page,
single item page, with add on choice and modifier
cart page(to include recommended items, ordered item list, remove item total, changeable quantity,
confirmation page(success, fail)

DELIVERABLES - responsive html, fonts, images asset such as icons, animation, button images(suitable for commercial use without further third party loyalty fee)

Hi all if we have left a comment on ur design, please revise accordingly and we will conclude it soon!

Target Market(s)

young diners who order food on their mobile phone.

Industry/Entity Type

Restaurant

Coding

Coded - Design and coding required

Number of Pages Required

5+ page

Colors

Designer to choose colors to be used in the design.

Requirements
Must have
• - lively, appetising colors while making the page easy to read. easy on eyes.
• - consistency. fonts used.
Nice to have
• - 2 color schemes
• - html codes. we will top up if you can deliver coded html.
Should not have
• - should not have more than 3 colors
• - should not have more than 3 different fonts
• - should not use colors that are dull

```html
<!DOCTYPE html>
<html lang="en">
<head>
<meta charset="utf-8">
<meta name="viewport" content="width=1200, user-scalable=no">
<title>Pesanly – Vegetable Menu</title>
<link href="https://fonts.googleapis.com/css2?family=Mulish:wght@400;600;700;800&family=Noto+Sans+SC:wght@400;600&display=swap" rel="stylesheet">
<style>
  :root {
    --brand: #16b98f;
    --brand-dark: #1f2b2d;
    --ink: #232a2c;
    --muted: #7c8386;
    --surface: #ffffff;
    --page: #ffffff;
  }
  * { box-sizing: border-box; margin: 0; padding: 0; }
  html, body {
    width: 1200px; height: 904px; overflow: hidden;
    background: var(--page);
    font-family: "Mulish", "Noto Sans SC", sans-serif;
    color: var(--ink);
  }
  .app { position: relative; width: 1200px; height: 904px; overflow: hidden; }

  /* Sidebar */
  .sidebar {
    position: absolute; left: 0; top: 0; width: 355px; height: 904px;
    background: var(--brand);
  }
  .brand {
    position: absolute; left: 96px; top: 28px;
    font-size: 36px; font-weight: 800; color: #fff; letter-spacing: 0.5px;
  }
  .categories { list-style: none; position: absolute; left: 95px; top: 92px; width: 260px; }
  .category {
    display: flex; align-items: center; height: 56px; margin-bottom: 9px;
    padding-left: 26px; color: #fff; font-size: 22px; font-weight: 600;
  }
  .category svg { width: 26px; height: 26px; margin-right: 20px; flex: none; }
  .category.is-active { background: var(--brand-dark); }

  /* Main */
  .main { position: absolute; left: 389px; top: 0; width: 811px; height: 904px; }
  .page-title { position: absolute; left: 0; top: 26px; font-size: 29px; font-weight: 800; }
  .cart { position: absolute; left: 733px; top: 36px; width: 34px; height: 32px; }
  .cart-badge {
    position: absolute; left: 757px; top: 33px; width: 18px; height: 18px;
    border-radius: 50%; background: var(--brand); color: #fff;
    font-size: 9px; font-weight: 800; display: flex; align-items: center; justify-content: center;
  }

  .menu-grid {
    position: absolute; left: 0; top: 94px;
    display: grid; grid-template-columns: repeat(3, 235px);
    column-gap: 27px; row-gap: 24px;
  }
  .dish {
    width: 235px; height: 274px; background: var(--surface);
    box-shadow: 0 2px 8px rgba(0,0,0,0.18);
  }
  .dish-photo { height: 163px; }
  .dish-info { padding: 16px 17px 0; }
  .dish-name { font-size: 15px; font-weight: 700; line-height: 1.2; }
  .dish-alt { font-size: 13px; color: var(--muted); margin-top: 7px; }
  .dish-price { font-size: 19px; font-weight: 800; color: var(--brand); margin-top: 12px; }

  .photo-lettuce { background: linear-gradient(135deg, #c8e2a2, #8fbf5c 55%, #6a4a2c); }
  .photo-oyster { background: linear-gradient(135deg, #b08a5c, #6d4b2c 60%, #3f2a1a); }
  .photo-shitake { background: linear-gradient(135deg, #7a4a2a, #3e2416 60%, #a5683b); }
  .photo-bean { background: linear-gradient(135deg, #6fae3c, #3f8a22 60%, #6a4a2c); }
  .photo-eryngii { background: linear-gradient(135deg, #f0c450, #d49a2c 60%, #7a5230); }
  .photo-potato { background: linear-gradient(135deg, #e8c96a, #c99a3a 60%, #6a4a2c); }
  .photo-corn { background: linear-gradient(135deg, #f2c94c, #d9a328 60%, #6a4a2c); }
  .photo-toast { background: linear-gradient(135deg, #e0a868, #b8743a 60%, #5a3a22); }
</style>
</head>
<body>
<div class="app">
  <aside class="sidebar">
    <div class="brand">Pesanly</div>
    <ul class="categories">
      <li class="category is-active">
        <svg viewBox="0 0 26 26" fill="none" stroke="#fff" stroke-width="1.6"><path d="M6 5c4 2 4 8 0 10M20 5c-4 2-4 8 0 10M6 21c4-2 10-2 14 0M13 4v18"/></svg>Vegetable</li>
      <li class="category">
        <svg viewBox="0 0 26 26" fill="none" stroke="#fff" stroke-width="1.6"><ellipse cx="13" cy="13" rx="10" ry="7"/><circle cx="9" cy="12" r="2"/></svg>Meat</li>
      <li class="category">
        <svg viewBox="0 0 26 26" fill="none" stroke="#fff" stroke-width="1.6"><path d="M18 4c-7 0-11 5-11 10 0 4 3 7 7 7M7 14c-2 2-3 4-2 7"/></svg>Seafood</li>
      <li class="category">
        <svg viewBox="0 0 26 26" fill="none" stroke="#fff" stroke-width="1.6"><path d="M4 20h18M6 20c0-5 3-9 7-9s7 4 7 9M13 11V6"/></svg>Special</li>
      <li class="category">
        <svg viewBox="0 0 26 26" fill="none" stroke="#fff" stroke-width="1.6"><path d="M3 19h20M5 19c0-5 4-9 8-9s8 4 8 9M13 10V7"/></svg>Cold Dish</li>
      <li class="category">
        <svg viewBox="0 0 26 26" fill="none" stroke="#fff" stroke-width="1.6"><circle cx="13" cy="13" r="10"/><path d="M10 7v12M16 7v12"/></svg>Main</li>
      <li class="category">
        <svg viewBox="0 0 26 26" fill="none" stroke="#fff" stroke-width="1.6"><circle cx="13" cy="13" r="10"/><path d="M6 18L18 6"/></svg>Set</li>
      <li class="category">
        <svg viewBox="0 0 26 26" fill="none" stroke="#fff" stroke-width="1.6"><path d="M6 10h12l-2 12H8zM14 10l3-7"/></svg>Juice</li>
      <li class="category">
        <svg viewBox="0 0 26 26" fill="none" stroke="#fff" stroke-width="1.6"><path d="M7 3h5v7a2.5 2.5 0 0 1-5 0zM9.5 12v10M14 3h5v7a2.5 2.5 0 0 1-5 0zM16.5 12v10"/></svg>Drink</li>
      <li class="category">
        <svg viewBox="0 0 26 26" fill="none" stroke="#fff" stroke-width="1.6"><rect x="6" y="6" width="11" height="16" rx="1"/><path d="M17 10h3v7h-3"/></svg>Beer</li>
      <li class="category">
        <svg viewBox="0 0 26 26" fill="none" stroke="#fff" stroke-width="1.6"><path d="M5 12h16l-2 10H7zM9 12V7M17 12V7"/></svg>Alcohol</li>
      <li class="category">
        <svg viewBox="0 0 26 26" fill="none" stroke="#fff" stroke-width="1.6"><path d="M8 4h10v5a5 5 0 0 1-10 0zM13 14v6M9 22h8"/></svg>Wine</li>
    </ul>
  </aside>

  <main class="main">
    <h1 class="page-title">Vegetable</h1>
    <svg class="cart" viewBox="0 0 34 32" fill="none" stroke="#232a2c" stroke-width="1.8" stroke-linejoin="round">
      <path d="M1 4h5l4 17h17l4-12H8"/><circle cx="12" cy="27" r="2"/><circle cx="25" cy="27" r="2"/>
    </svg>
    <div class="cart-badge">02</div>

    <section class="menu-grid">
      <article class="dish">
        <div class="dish-photo photo-lettuce" role="img" aria-label="Grilled romaine lettuce skewers"></div>
        <div class="dish-info"><h2 class="dish-name">Grilled Romaine Lettuce</h2><p class="dish-alt">烤油麦菜</p><p class="dish-price">S$1.30</p></div>
      </article>
      <article class="dish">
        <div class="dish-photo photo-oyster" role="img" aria-label="Grilled oyster mushroom skewers"></div>
        <div class="dish-info"><h2 class="dish-name">Grilled Oyster Mushroom</h2><p class="dish-alt">烤鲜耗菇</p><p class="dish-price">S$1.30</p></div>
      </article>
      <article class="dish">
        <div class="dish-photo photo-shitake" role="img" aria-label="Grilled shitake mushroom skewers"></div>
        <div class="dish-info"><h2 class="dish-name">烤香菇</h2><p class="dish-alt">Grilled Shitake Mushroom</p><p class="dish-price">S$1.30</p></div>
      </article>
      <article class="dish">
        <div class="dish-photo photo-bean" role="img" aria-label="Grilled string bean skewers"></div>
        <div class="dish-info"><h2 class="dish-name">Grilled String Bean</h2><p class="dish-alt">烤四季豆</p><p class="dish-price">S$1.30</p></div>
      </article>
      <article class="dish">
        <div class="dish-photo photo-eryngii" role="img" aria-label="Grilled king oyster mushroom slices"></div>
        <div class="dish-info"><h2 class="dish-name">Grilled Pleurotus Eryngii</h2><p class="dish-alt">烤杏鲍菇</p><p class="dish-price">S$1.30</p></div>
      </article>
      <article class="dish">
        <div class="dish-photo photo-potato" role="img" aria-label="Grilled potato chip skewers"></div>
        <div class="dish-info"><h2 class="dish-name">Grilled Potato Chip 3Pcs</h2><p class="dish-alt">烤土豆片 3pcs</p><p class="dish-price">S$2.60</p></div>
      </article>
      <article class="dish">
        <div class="dish-photo photo-potato" role="img" aria-label="Grilled dry soya bean cake skewers"></div>
        <div class="dish-info"><h2 class="dish-name">Grilled Dry Soya Bean Cake 3Pcs</h2></div>
      </article>
      <article class="dish">
        <div class="dish-photo photo-corn" role="img" aria-label="Grilled corn on skewers"></div>
        <div class="dish-info"><h2 class="dish-name">Grilled Romaine Lettuce</h2><p class="dish-alt">烤油麦菜</p></div>
      </article>
      <article class="dish">
        <div class="dish-photo photo-toast" role="img" aria-label="Grilled toast slices"></div>
        <div class="dish-info"><h2 class="dish-name">Grilled Romaine Lettuce</h2></div>
      </article>
    </section>
  </main>
</div>
</body>
</html>
```